BrightNest

Need a 6 page template designed in Layered PSD for a house cleaning company.

Target Market(s)

People who are selling their homes and need house cleaning

Industry/Entity Type

House cleaning

Number of Pages Required

5+ page

Font styles to use
Sans Serif

Requirements
Must have
• Please see the zip file included with the brief. It has a document with detailed instructions.

```html
<!DOCTYPE html>
<html lang="en">
<head>
<meta charset="utf-8">
<title>BrightNest – Deep Pre-Sale, Move-In &amp; Move-Out Cleaning</title>
<link href="https://fonts.googleapis.com/css2?family=Montserrat:wght@400;500;600;700&family=Roboto+Condensed:wght@700&display=swap" rel="stylesheet">
<style>
:root{
  --blue:#2b4c9b;
  --navy:#1b2f6c;
  --green:#7ac143;
  --green-dark:#5fa32c;
  --grey:#dcdedd;
  --text:#3a3a3a;
  --white:#fff;
}
*{box-sizing:border-box;margin:0;padding:0}
html,body{width:1200px;height:4373px;overflow:hidden}
body{position:relative;font-family:'Montserrat',sans-serif;color:var(--text);background:var(--white)}
.abs{position:absolute}
.cond{font-family:'Roboto Condensed',sans-serif;font-weight:700}

/* header */
.site-header{position:absolute;left:0;top:0;width:1200px;height:76px;background:var(--white);z-index:3}
.brand{position:absolute;left:62px;top:14px;display:flex;align-items:center;gap:8px;font-size:28px;font-weight:700;color:var(--blue)}
.brand-dot{width:12px;height:12px;background:var(--green);border-radius:50%}
.main-nav{position:absolute;right:50px;top:54px;display:flex;gap:46px;font-size:13px;font-weight:500;color:#222}
.main-nav .current{border-bottom:2px solid var(--green)}
.quote-btn{position:absolute;left:740px;top:8px;width:182px;height:34px;background:var(--green);color:#fff;font-size:13px;display:flex;align-items:center;justify-content:center;border-radius:3px}
.call-box{position:absolute;left:953px;top:6px;width:184px;height:38px;background:var(--navy);color:#fff;border-radius:3px;display:flex;align-items:center;padding-left:12px;gap:8px}
.call-box small{display:block;font-size:9px;color:var(--green)}
.call-box b{font-size:14px}

/* hero */
.hero{position:absolute;left:0;top:76px;width:1200px;height:690px;background:linear-gradient(90deg,#6f6660,#9a948e 45%,#c9c6c2);overflow:hidden}
.hero-title{position:absolute;left:63px;top:170px;font-size:40px;line-height:51px;color:#fff;text-transform:uppercase;letter-spacing:1px;text-shadow:0 2px 4px rgba(0,0,0,.4)}
.pill{display:flex;align-items:center;justify-content:center;background:var(--green);color:#0d2a14;border:3px solid #fff;box-shadow:0 0 0 2px var(--green);border-radius:30px}
.hero-cta{position:absolute;left:250px;top:404px;width:268px;height:44px;font-size:22px}
.mascot{position:absolute;left:640px;top:40px;width:560px;height:580px;background:radial-gradient(ellipse at center,#3f73c4 0%,#6a93cf 45%,rgba(160,170,180,0) 72%)}

/* services */
.services{position:absolute;left:0;top:690px;width:1200px;height:820px;background:linear-gradient(#e8e9ea,#d9dcdf)}
.sec-title{position:absolute;width:1200px;text-align:center;font-size:30px;font-weight:500;color:var(--blue)}
.card{position:absolute;top:218px;width:259px;height:397px;color:#fff;border-radius:3px;text-align:center;padding:20px 12px}
.card.blue{background:rgba(27,55,130,.88)}
.card.green{background:rgba(78,140,40,.85)}
.card-tag{border:1.5px solid #fff;height:40px;display:flex;align-items:center;justify-content:center;font-size:17px;letter-spacing:.5px;margin:0 2px}
.card h3{font-size:14px;font-weight:600;line-height:16px;margin:13px 0 6px}
.card p{font-size:11px;line-height:15.5px}
.card .pill{position:absolute;left:52px;bottom:26px;width:155px;height:32px;font-size:15px;font-weight:500}

/* areas */
.areas-list{position:absolute;top:1720px;font-size:29px;line-height:60px;color:var(--blue)}
.areas-list.left{right:860px;text-align:right}
.areas-list.right{left:745px}
.bullet{display:inline-block;width:11px;height:11px;background:linear-gradient(var(--blue) 0 0) 0 0/4px 4px no-repeat,linear-gradient(var(--blue) 0 0) 7px 0/4px 4px no-repeat,linear-gradient(var(--blue) 0 0) 0 7px/4px 4px no-repeat,linear-gradient(var(--blue) 0 0) 7px 7px/4px 4px no-repeat;margin:0 10px;vertical-align:middle}
.area-art{position:absolute;left:405px;top:1655px;width:305px;height:615px;background:linear-gradient(160deg,#e3ecf8,#f6f1e2);border-radius:6px}

/* before/after */
.gallery{position:absolute;left:0;top:2410px;width:1200px;height:495px;background:var(--grey)}
.shot{position:absolute;top:157px;width:255px;height:262px}
.shot .img{height:223px}
.shot .lab{height:39px;color:#fff;font-size:22px;font-weight:600;display:flex;align-items:center;justify-content:center}

/* steps */
.step{position:absolute;top:3100px;width:200px;text-align:center}
.ring{width:190px;height:190px;margin:0 auto;border-radius:50%;border:4px solid var(--green);position:relative}
.ring .img{position:absolute;inset:8px;border-radius:50%}
.num{position:absolute;width:36px;height:36px;border-radius:50%;background:var(--green);color:#fff;font-weight:700;font-size:22px;display:flex;align-items:center;justify-content:center;border:3px solid #fff}
.step h4{font-size:15px;font-weight:500;color:var(--blue);margin-top:12px}
.step p{font-size:12px;line-height:15px}

/* blog */
.post{position:absolute;top:3495px;width:253px;height:151px;background:#e5e5e5;display:flex}
.post .img{width:121px;height:151px}
.post .date{position:absolute;left:105px;top:20px;width:92px;height:19px;border-radius:10px;background:var(--navy);color:#fff;font-size:10px;display:flex;align-items:center;justify-content:center}
.post p{position:absolute;left:128px;top:52px;width:118px;font-size:12px;line-height:15px}

/* contact */
.contact{position:absolute;left:0;top:3805px;width:1200px;height:316px;background:var(--green)}
.field{position:absolute;background:#e9e9e9;border:1px solid #fff;font-size:12px;padding:3px 8px;color:#444}
.send{position:absolute;left:606px;top:215px;width:80px;height:26px;background:var(--navy);color:#fff;font-size:12px;display:flex;align-items:center;justify-content:center}

/* footer */
.site-footer{position:absolute;left:0;top:4121px;width:1200px;height:252px;background:var(--navy);color:#fff}
.site-footer h5{font-size:15px;font-weight:600;color:var(--green);margin-bottom:10px}
.foot-col{position:absolute;top:26px;font-size:11px;line-height:23px}
.copy{position:absolute;bottom:8px;width:1200px;text-align:center;font-size:10px;color:#9fb0d6}
</style>
</head>
<body>

<header class="site-header">
  <div class="brand"><span class="brand-dot"></span>BrightNest</div>
  <div class="quote-btn cond">GET ONLINE QUOTES</div>
  <div class="call-box">
    <svg width="20" height="20" viewBox="0 0 24 24"><path fill="#7ac143" d="M6.6 10.8a15 15 0 006.6 6.6l2.2-2.2a1 1 0 011-.25 11 11 0 003.6.6 1 1 0 011 1V20a1 1 0 01-1 1A17 17 0 013 4a1 1 0 011-1h3.5a1 1 0 011 1 11 11 0 00.6 3.6 1 1 0 01-.25 1z"/></svg>
    <div><small>Contact Us Today!</small><b>(XXX) XXXX XXXX</b></div>
  </div>
  <nav class="main-nav">
    <span class="current">HOME</span><span>SERVICES</span><span>WHAT'S INCLUDED</span><span>FOR REALTORS</span><span>BLOG</span><span>CONTACT</span>
  </nav>
</header>

<section class="hero">
  <div class="mascot" role="img" aria-label="Cartoon cleaner mascot in blue overalls holding a mop"></div>
  <h1 class="hero-title cond">The only Barrie area cleaning<br>service that specializes in deep<br>pre-sale, move-in, &amp; move-out<br>house cleanings</h1>
  <div class="pill hero-cta">CONTACT US</div>
</section>

<section class="services" role="img" aria-label="Faded photo of cleaners working in a home">
  <h2 class="sec-title" style="top:125px">CLEANING SERVICES WE OFFER</h2>
  <div class="card blue" style="left:60px">
    <div class="card-tag cond">PRE-SALE CLEANING</div>
    <h3>Are You Putting Your Barrie Area Home Up for Sale?</h3>
    <p>First impressions matter, and a clean and fresh home can make a huge difference. At BrightNest.com, we specialize in deep cleaning services that will get your home in tip-top shape for potential buyers. Not only will a move-out deep cleaning make your home more attractive to potential buyers, but it can also increase its value. A well-maintained home is a valuable asset that can command a higher price...</p>
    <div class="pill">LEARN MORE</div>
  </div>
  <div class="card green" style="left:333px">
    <div class="card-tag cond">MOVE-IN CLEANINGS</div>
    <h3>Take the Stress Out of Your Move &amp; Have Your Home Sparkling Clean Before You Move In</h3>
    <p>Moving doesn't have to be a stressful experience. Let us take the hassle out of your move and ensure your new Barrie home is clean, fresh, and ready for you to settle in. Our Barrie area move-in deep cleaning service is designed so that you can start your new chapter with a spotless and hygienic environment. Our experienced and skilled cleaners will work diligently to ensure that every nook...</p>
    <div class="pill">LEARN MORE</div>
  </div>
  <div class="card blue" style="left:607px">
    <div class="card-tag cond">MOVE-OUT CLEANINGS</div>
    <h3>Cleaned &amp; Ready for The Next Occupants</h3>
    <p>Looking for a professional move-out cleaning service to ensure that your property is left sparkling clean and ready for the next occupants? Look no further than our expert team of cleaning professionals! At BrightNest.com, we provide move-out cleaning services to homeowners and tenants throughout the Barrie area. Our team of experienced and fully trained cleaners will work tirelessly ...</p>
    <div class="pill">LEARN MORE</div>
  </div>
  <div class="card green" style="left:881px">
    <div class="card-tag cond">JUNK REMOVAL</div>
    <h3>The Only Barrie Area Cleaning Service That Specializes in Deep Pre-Sale, Move-In &amp; Move-Out House Cleanings</h3>
    <p>Whether you're moving into or out of a Barrie area home, apartment, or rental property, our Barrie area Pre-Sale, Move-In, and Move-Out Deep Cleaning Services are the perfect solution for you. Contact us today to schedule an appointment, and let us take care of the daunting task of having your home deep cleaned...</p>
    <div class="pill">LEARN MORE</div>
  </div>
</section>

<svg class="abs" style="left:0;top:620px" width="1200" height="160" viewBox="0 0 1200 160">
  <path d="M0 70 C120 150 280 150 440 105 C640 50 800 30 1000 80 C1100 105 1160 95 1200 80 L1200 160 L0 160Z" fill="#e8e9ea"/>
  <path d="M0 70 C120 150 280 150 440 105 C640 50 800 30 1000 80 C1100 105 1160 95 1200 80 L1200 100 C1150 112 1090 118 1000 96 C800 48 640 68 440 122 C280 162 120 160 0 92Z" fill="#7ac143"/>
</svg>

<svg class="abs" style="left:0;top:1400px" width="1200" height="150" viewBox="0 0 1200 150">
  <path d="M0 60 C150 30 260 100 420 115 C650 135 900 40 1200 70 L1200 150 L0 150Z" fill="#fff"/>
  <path d="M40 75 C200 110 330 150 520 138 C760 120 950 60 1200 80 L1200 88 C960 80 780 140 520 150 C320 158 180 130 40 75Z" fill="#1b2f6c"/>
</svg>

<h2 class="sec-title" style="top:1573px">AREAS WE SERVICE</h2>
<div class="areas-list left cond">
  <div>Barrie<span class="bullet"></span></div><div>Innisfil<span class="bullet"></span></div><div>Springwater<span class="bullet"></span></div><div>Minesing<span class="bullet"></span></div><div>Orillia<span class="bullet"></span></div><div>Wasaga<span class="bullet"></span></div><div>Midland<span class="bullet"></span></div><div>Angus<span class="bullet"></span></div><div>Collingwood<span class="bullet"></span></div>
</div>
<div class="area-art" role="img" aria-label="Illustration of a cleaner leaning on a broom beside a mop bucket"></div>
<div class="areas-list right cond">
  <div><span class="bullet"></span>New Lowell</div><div><span class="bullet"></span>Oro-Medonte</div><div><span class="bullet"></span>Shanty Bay</div><div><span class="bullet"></span>Horseshoe Valley</div><div><span class="bullet"></span>Coldwater</div><div><span class="bullet"></span>Stayner</div><div><span class="bullet"></span>Creemore</div><div><span class="bullet"></span>Alliston</div><div><span class="bullet"></span>And everywhere in between</div>
</div>

<section class="gallery">
  <h2 class="sec-title" style="top:70px">BEFOR &amp; AFTER PICTURE</h2>
  <div class="shot" style="left:68px"><div class="img" role="img" aria-label="Kitchen before cleaning with boxes" style="background:linear-gradient(#d8d8d6,#8c8e90)"></div><div class="lab" style="background:var(--green)">BEFOR</div></div>
  <div class="shot" style="left:330px"><div class="img" role="img" aria-label="Kitchen after cleaning" style="background:linear-gradient(#f1f1f0,#6e7074)"></div><div class="lab" style="background:var(--blue)">AFTER</div></div>
  <div class="shot" style="left:616px"><div class="img" role="img" aria-label="Living room before cleaning with boxes" style="background:linear-gradient(90deg,#e2e0dc,#3a3c40 60%,#cfcfcd)"></div><div class="lab" style="background:var(--green)">BEFOR</div></div>
  <div class="shot" style="left:879px"><div class="img" role="img" aria-label="Living room after cleaning" style="background:linear-gradient(90deg,#ececea,#3a3c40 60%,#d6d6d4)"></div><div class="lab" style="background:var(--blue)">AFTER</div></div>
</section>

<h2 class="sec-title" style="top:2972px">HOW BRIGHTNEST CLEANS</h2>
<svg class="abs" style="left:330px;top:3195px" width="540" height="4"><rect width="540" height="3" fill="#7ac143"/></svg>
<div class="step" style="left:230px">
  <div class="ring"><div class="img" role="img" aria-label="Hands typing on a laptop" style="background:linear-gradient(#ececec,#9aa0a8)"></div><div class="num" style="left:77px;top:-18px">1</div></div>
  <h4>Book Online</h4><p>Lorem ipsum dolor sit amet,<br>consectetur adipiscing elit.</p>
</div>
<div class="step" style="left:500px">
  <div class="ring"><div class="img" role="img" aria-label="Mop cleaning a floor beside a bucket" style="background:linear-gradient(#e8eef2,#c7d3da)"></div><div class="num" style="left:77px;bottom:-18px">2</div></div>
  <h4>Clean</h4><p>Lorem ipsum dolor sit amet,<br>consectetur adipiscing elit.</p>
</div>
<div class="step" style="left:770px">
  <div class="ring"><div class="img" role="img" aria-label="Person relaxing in an armchair" style="background:linear-gradient(#f3f5f6,#b6c2cc)"></div><div class="num" style="left:77px;top:-18px">3</div></div>
  <h4>Relax</h4><p>Lorem ipsum dolor sit amet,<br>consectetur adipiscing elit.</p>
</div>

<h2 class="sec-title" style="top:3422px">READ OUR BLOG</h2>
<div class="post" style="left:60px"><div class="img" role="img" aria-label="Worker cleaning with equipment" style="background:linear-gradient(#cfcfcd,#6b6760)"></div><span class="date">27-02-2023</span><p>Lorem ipsu myh a dolor sit amet tay, consect eturqw ie adipiscing elit.</p></div>
<div class="post" style="left:335px"><div class="img" role="img" aria-label="Mover carrying a box" style="background:linear-gradient(#eeeeec,#b08a5a)"></div><span class="date">27-02-2023</span><p>Lorem ipsu myh a dolor sit amet tay, consect eturqw ie adipiscing elit.</p></div>
<div class="post" style="left:608px"><div class="img" role="img" aria-label="Mop and bucket on a floor" style="background:linear-gradient(#f0f0ef,#9fb0a8)"></div><span class="date">27-02-2023</span><p>Lorem ipsu myh a dolor sit amet tay, consect eturqw ie adipiscing elit.</p></div>
<div class="post" style="left:882px"><div class="img" role="img" aria-label="Pile of junk and scrap" style="background:linear-gradient(#8e8a84,#4a4844)"></div><span class="date">27-02-2023</span><p>Lorem ipsu myh a dolor sit amet tay, consect eturqw ie adipiscing elit.</p></div>
<div class="pill abs" style="left:467px;top:3683px;width:268px;height:44px;font-size:22px">VIEW ALL BLOG</div>

<section class="contact">
  <h2 class="sec-title" style="top:70px;color:#fff">CONTACT US</h2>
  <div class="field" style="left:343px;top:135px;width:251px;height:26px">Name</div>
  <div class="field" style="left:343px;top:175px;width:251px;height:26px">Tel no.</div>
  <div class="field" style="left:343px;top:215px;width:251px;height:26px">Email</div>
  <div class="field" style="left:606px;top:135px;width:252px;height:66px">Name</div>
  <div class="send">SEND</div>
</section>

<footer class="site-footer">
  <div class="abs" style="left:70px;top:40px;font-size:26px;font-weight:700;display:flex;align-items:center;gap:8px"><span class="brand-dot"></span>BrightNest</div>
  <div class="abs" style="left:70px;top:100px;display:flex;gap:16px">
    <span style="width:16px;height:16px;background:var(--green);border-radius:50%"></span>
    <span style="width:16px;height:16px;background:var(--green);border-radius:50%"></span>
    <span style="width:16px;height:16px;background:var(--green);border-radius:50%"></span>
  </div>
  <div class="foot-col" style="left:311px"><h5>Link</h5>Home<br>Services<br>What's Included<br>For Realtors<br>Blog<br>Contact</div>
  <div class="foot-col" style="left:589px"><h5>We Open</h5>Open 7 Days a Week (Monday-Sunday)<br>Hours 8:00 am – 9:00 pm<br>Evenings &amp; Weekends (Yes)<br>Short Notice (Yes)</div>
  <div class="foot-col" style="left:953px;line-height:16px"><h5>BrightNest</h5>
    <div style="display:flex;gap:8px;margin-bottom:12px"><svg width="14" height="18" viewBox="0 0 14 18"><path d="M7 0a7 7 0 00-7 7c0 5 7 11 7 11s7-6 7-11a7 7 0 00-7-7zm0 10a3 3 0 110-6 3 3 0 010 6z" fill="#7ac143"/></svg><span>Lorem ipsum dolor sit amet,<br>consectetur adipiscing elit</span></div>
    <div style="display:flex;gap:8px;margin-bottom:12px"><svg width="16" height="12" viewBox="0 0 16 12"><rect width="16" height="12" fill="#7ac143"/><path d="M0 0l8 7 8-7" stroke="#1b2f6c" fill="none"/></svg><span>info@brightnest.com</span></div>
    <div style="display:flex;gap:8px"><svg width="16" height="16" viewBox="0 0 24 24"><path fill="#7ac143" d="M6.6 10.8a15 15 0 006.6 6.6l2.2-2.2a1 1 0 011-.25 11 11 0 003.6.6 1 1 0 011 1V20a1 1 0 01-1 1A17 17 0 013 4a1 1 0 011-1h3.5a1 1 0 011 1 11 11 0 00.6 3.6 1 1 0 01-.25 1z"/></svg><span>(XXX) XXXX XXXX</span></div>
  </div>
  <div class="copy">Copyright © 2023 BrightNest. All rights reserved.</div>
</footer>

</body>
</html>
```